Korvel Professional Services Website

Small website for company presence and information. Company is an IT/Telecom services company. We provide presales and installation services. Included are various company logos including color levels. Site doesn't have to use these exact colors in the logos, but should be complimentary if using different colors. It should have a professional business appearance.
Updates

My apologies for not being more responsive on the designs that have been submitted. I will be narrowing down the submissions and providing additional feedback next week. Thank you for your patience.

Project Deadline Extended
Reason: Sorry again for delays on picking designs. Work has me very busy and I've just not had the time to devote to this project. I am extending the design deadline for a few more days to give me time to make my final decisions. Thank you all for your patience. Stay tuned....

Target Market(s)

Telecom sales companies that sell Quenti telecom products.

Industry/Entity Type

Professional Service

Coding

Coded - Design and coding required

Number of Pages Required

5+ page

Font styles to use
Sans Serif

Colors
3276b5
0355a3
85abd2
85cae6
33a6d7
0692cd
ffffff

Requirements
Must have
• Professional design reflective of IT/Telecom business. A good reference website would be: http://www.lorbextech.example/. Looking for something similar in function and presence.
Nice to have
• Rolling photos highlighting our services. Traditional navigation across the top of all pages.
Should not have
• No motion video, flashy presentation or overly confused interface.

```html
<!DOCTYPE html>
<html lang="en">
<head>
<meta charset="utf-8">
<title>Korvel Professional Services</title>
<link href="https://fonts.googleapis.com/css2?family=Roboto:wght@400;500;700&family=Source+Sans+3:wght@400;600&display=swap" rel="stylesheet">
<style>
:root{
  --navy:#0a2a66;
  --blue:#0355a3;
  --bright:#0a6fb5;
  --sky:#85abd2;
  --ink:#2d3440;
  --muted:#5b6470;
  --line:#d4d8de;
  --band:#032a66;
  --footer:#050a1f;
  --white:#ffffff;
  --mark:#0d3f86;
}
*{box-sizing:border-box;margin:0;padding:0}
html,body{width:1200px;height:3637px;overflow:hidden;background:var(--white)}
body{position:relative;font-family:"Source Sans 3",Arial,sans-serif;color:var(--ink)}
.abs{position:absolute}
/* header */
.site-header{left:0;top:0;width:1200px;height:94px;background:var(--white)}
.brand{left:64px;top:22px;display:flex;align-items:center;gap:10px}
.brand-square{width:40px;height:40px;background:var(--mark);border-radius:4px}
.brand-name{width:160px;font-family:"Roboto",sans-serif;font-weight:700;font-size:15px;line-height:18px;color:var(--mark);letter-spacing:.5px}
.main-nav a{position:absolute;top:38px;font-family:"Roboto",sans-serif;font-size:16px;color:var(--ink);text-decoration:none}
.main-nav .active::after{content:"";position:absolute;left:50%;top:26px;width:6px;height:6px;margin-left:-3px;border-radius:50%;background:var(--navy)}
.main-nav .nav-cta{top:34px;padding:5px 12px;background:var(--bright);color:var(--white);border-radius:14px}
/* hero */
.hero{left:0;top:94px;width:1200px;height:529px;background:linear-gradient(100deg,#41536f 0%,#6d7f99 40%,#46586f 70%,#2f3f57 100%)}
.hero-title{left:139px;top:186px;width:700px;font-family:"Roboto",sans-serif;font-weight:700;font-size:43px;line-height:49px;color:var(--white)}
.hero-text{left:139px;top:302px;width:440px;font-size:24px;line-height:25px;color:var(--white)}
.btn{display:block;text-align:center;background:var(--bright);color:var(--white);font-family:"Roboto",sans-serif;font-size:15px;border-radius:16px;text-decoration:none}
.hero-btn{left:139px;top:378px;width:128px;height:30px;line-height:30px}
.slide-arrow{top:215px;width:24px;height:100px;background:rgba(200,205,212,.55);display:flex;align-items:center;justify-content:center}
/* sections */
.section-mark{left:575px;width:50px;height:50px;background:var(--mark);border-radius:6px}
.section-title{left:0;width:1200px;text-align:center;font-family:"Roboto",sans-serif;font-weight:400;font-size:26px;color:var(--navy)}
.about-text{left:156px;width:888px;font-size:20px;line-height:23px;text-align:center;color:var(--ink)}
.about-btn{left:547px;top:1081px;width:128px;height:30px;line-height:30px}
.statement{left:0;top:1155px;width:1200px;height:174px;background:var(--band)}
.statement p{position:absolute;left:150px;top:48px;width:900px;text-align:center;font-size:15px;line-height:20px;color:var(--white)}
.service{width:300px;height:87px;display:flex;gap:22px}
.service-icon{width:87px;height:87px;border:3px solid var(--bright);display:flex;align-items:center;justify-content:center;flex:none}
.service h3{font-family:"Roboto",sans-serif;font-weight:400;font-size:16px;color:var(--ink);margin-top:11px}
.service p{font-family:"Roboto",sans-serif;font-size:12.5px;line-height:15px;color:var(--ink);margin-top:6px;width:170px}
.divider{left:59px;width:1079px;height:1px;background:var(--line)}
.presales-intro{left:100px;top:1946px;width:1000px;text-align:center;font-size:15.5px;line-height:18px;color:var(--ink)}
.circuit-field{left:792px;top:1843px;width:408px;height:544px;background:radial-gradient(circle at 70% 40%,rgba(133,171,210,.35),rgba(255,255,255,0) 70%)}
.presale{width:270px;text-align:center}
.presale-photo{width:228px;height:228px;border-radius:50%;margin:0 auto}
.presale h3{margin-top:20px;font-family:"Roboto",sans-serif;font-weight:700;font-size:15px;color:var(--bright)}
.presale p{margin:8px auto 0;width:250px;font-size:12.5px;line-height:15px;color:var(--muted)}
.partner-badge{width:210px;height:64px;border-radius:32px;background:#c9ccd1}
.contact-field{left:0;top:2895px;width:620px;height:420px;background:radial-gradient(ellipse at 25% 50%,rgba(133,171,210,.32),rgba(255,255,255,0) 72%)}
.field{left:59px;width:542px;border:1px solid #b9bec6;background:rgba(255,255,255,.85);font-size:10px;color:#8a9099;padding:4px 6px}
.send-btn{left:260px;top:3248px;width:131px;height:33px;line-height:33px;border-radius:17px;font-size:17px}
.office{left:678px;top:3028px;font-family:"Roboto",sans-serif;font-size:21px;line-height:26px;color:var(--ink)}
.office h3{font-weight:700;font-size:22px;margin-bottom:30px}
.office .gap{margin-top:28px}
.to-top{left:1141px;top:3281px;width:24px;height:24px;border-radius:50%;background:var(--bright);display:flex;align-items:center;justify-content:center}
.site-footer{left:0;top:3320px;width:1200px;height:317px;background:var(--footer)}
.footer-brand{left:0;top:70px;width:1200px;display:flex;justify-content:center;align-items:center;gap:16px}
.footer-brand .sq{width:56px;height:56px;background:var(--white);border-radius:6px}
.footer-brand span{font-family:"Roboto",sans-serif;font-weight:700;font-size:40px;color:var(--white);letter-spacing:2px}
.social{top:193px;width:12px;height:12px;border-radius:50%;background:var(--white)}
.footer-nav a{position:absolute;top:236px;font-family:"Roboto",sans-serif;font-size:16px;color:var(--white);text-decoration:none}
</style>
</head>
<body>

<header class="site-header abs">
  <div class="brand abs"><div class="brand-square"></div><div class="brand-name">KORVEL PROFESSIONAL SERVICES</div></div>
  <nav class="main-nav">
    <a class="active" style="left:470px">Home</a>
    <a style="left:568px">Company</a>
    <a style="left:690px">Services</a>
    <a style="left:806px">Presales</a>
    <a style="left:925px">Partners</a>
    <a class="nav-cta" style="left:1034px">Contact Us</a>
  </nav>
</header>

<section class="hero abs" role="img" aria-label="Photo of business people walking in an office, overlaid with a network line pattern">
  <div class="slide-arrow abs" style="left:35px"><svg width="10" height="14"><path d="M8 1 2 7l6 6" stroke="#fff" stroke-width="2" fill="none"/></svg></div>
  <div class="slide-arrow abs" style="left:1141px"><svg width="10" height="14"><path d="M2 1l6 6-6 6" stroke="#fff" stroke-width="2" fill="none"/></svg></div>
  <h1 class="hero-title abs">Lorem ipsum dolor sit amet consectetur adipisicing elit</h1>
  <p class="hero-text abs">Accusantium doloremque laudantium totam rem aperiam, eaque ipsa...</p>
  <a class="btn hero-btn abs">Read more</a>
</section>

<div class="section-mark abs" style="top:660px"></div>
<h2 class="section-title abs" style="top:728px">About the company</h2>
<p class="about-text abs" style="top:787px">Lorem ipsum dolor sit amet, consectetur adipiscing elit. In at nibh placerat, vulputate velit vitae, imperdiet justo. In et quam tristique, aliquet enim vitae, pellentesque mauris. Nulla quis auctor nisi, a pretium turpis. Aenean risus erat, laoreet id aliquet vitae, ornare a augue. Sed et molestie dui. In fermentum bibendum nibh, at cursus nisi porttitor non. Aenean varius, libero eget pharetra finibus, eros mauris scelerisque nunc, quis egestas enim magna mollis massa. In pulvinar sed urna id fermentum. Interdum et malesuada fames ac ante ipsum primis in faucibus.</p>
<p class="about-text abs" style="top:968px">Nunc ac ex nec orci tincidunt maximus ac nec eros. Integer a turpis leo. Sed varius arcu enim, eget sagittis elit porttitor vel. Ut eget volutpat nisi. Fusce orci libero, venenatis eu hendrerit in, feugiat vel nibh. Nulla ac nulla neque. Nullam tincidunt leo tincidunt orci euismod sagittis.</p>
<a class="btn about-btn abs">Read more</a>

<section class="statement abs"><p>Quisque at fermentum justo. Aenean ullamcorper lorem nisl, quis suscipit urna iaculis vitae. Duis at tempor libero, a condimentum massa. Pellentesque aliquam feugiat erat, et commodo mauris varius non. Sed nec faucibus odio, ac porttitor libero. Phasellus sit amet posuere ante. Mauris imperdiet est viverra est mattis, quis ultrices libero interdum. Mauris turpis ante, aliquet nec orci vitae, cursus dignissim nibh. Donec in ullamcorper eros, non imperdiet ex.</p></section>

<div class="section-mark abs" style="top:1360px"></div>
<h2 class="section-title abs" style="top:1434px">Our Services</h2>

<svg width="0" height="0" style="position:absolute">
  <symbol id="cloud-signal" viewBox="0 0 64 40">
    <path d="M14 32h26a9 9 0 0 0 0-18 13 13 0 0 0-25-2A10 10 0 0 0 14 32z" fill="none" stroke="#0a6fb5" stroke-width="3"/>
    <path d="M49 14a10 10 0 0 1 0 14M54 10a16 16 0 0 1 0 22M59 6a22 22 0 0 1 0 30" fill="none" stroke="#0a6fb5" stroke-width="2.5" stroke-linecap="round"/>
  </symbol>
</svg>

<div class="service abs" style="left:136px;top:1519px"><div class="service-icon"><svg width="60" height="38"><use href="#cloud-signal"/></svg></div><div><h3>Fresh and Clean</h3><p>Lorem ipsum dolor sit amet, consectetur adipisicing elit</p></div></div>
<div class="service abs" style="left:465px;top:1519px"><div class="service-icon"><svg width="60" height="38"><use href="#cloud-signal"/></svg></div><div><h3>Fresh and Clean</h3><p>Lorem ipsum dolor sit amet, consectetur adipisicing elit</p></div></div>
<div class="service abs" style="left:792px;top:1519px"><div class="service-icon"><svg width="60" height="38"><use href="#cloud-signal"/></svg></div><div><h3>Fresh and Clean</h3><p>Lorem ipsum dolor sit amet, consectetur adipisicing elit</p></div></div>
<div class="service abs" style="left:136px;top:1667px"><div class="service-icon"><svg width="60" height="38"><use href="#cloud-signal"/></svg></div><div><h3>Fresh and Clean</h3><p>Lorem ipsum dolor sit amet, consectetur adipisicing elit</p></div></div>
<div class="service abs" style="left:465px;top:1667px"><div class="service-icon"><svg width="60" height="38"><use href="#cloud-signal"/></svg></div><div><h3>Fresh and Clean</h3><p>Lorem ipsum dolor sit amet, consectetur adipisicing elit</p></div></div>
<div class="service abs" style="left:792px;top:1667px"><div class="service-icon"><svg width="60" height="38"><use href="#cloud-signal"/></svg></div><div><h3>Fresh and Clean</h3><p>Lorem ipsum dolor sit amet, consectetur adipisicing elit</p></div></div>

<div class="divider abs" style="top:1813px"></div>

<div class="circuit-field abs" role="img" aria-label="Faint circuit line pattern"></div>
<div class="section-mark abs" style="top:1842px"></div>
<h2 class="section-title abs" style="top:1910px">Presales</h2>
<p class="presales-intro abs">Nunc ac ex nec orci tincidunt maximus ac nec eros. Integer a turpis leo. Sed varius arcu enim, eget sagittis elit porttitor vel. Ut eget volutpat nisi. Fusce orci libero, venenatis eu hendrerit in, feugiat vel nibh. Nulla ac nulla neque. Nullam tincidunt leo tincidunt orci euismod sagittis.</p>

<div class="presale abs" style="left:125px;top:2054px">
  <div class="presale-photo" role="img" aria-label="Photo of a telecom antenna tower against a blue sky" style="background:linear-gradient(160deg,#2a86c9,#0f5da4)"></div>
  <h3>Lorem ipsum dolor sit</h3>
  <p>Nunc ac ex nec orci tincidunt maximus ac nec eros. Integer a turpis leo. Sed varius arcu enim, eget sagittis elit porttitor vel. Ut eget volutpat nisi. Fusce orci libero, venenatis eu hendrerit in, feugiat vel nibh.</p>
</div>
<div class="presale abs" style="left:464px;top:2054px">
  <div class="presale-photo" role="img" aria-label="Photo of a technician using a handheld network tester" style="background:linear-gradient(160deg,#8d9299,#3e434a)"></div>
  <h3>Lorem ipsum dolor sit</h3>
  <p>Nunc ac ex nec orci tincidunt maximus ac nec eros. Integer a turpis leo. Sed varius arcu enim, eget sagittis elit porttitor vel. Ut eget volutpat nisi. Fusce orci libero, venenatis eu hendrerit in, feugiat vel nibh.</p>
</div>
<div class="presale abs" style="left:805px;top:2054px">
  <div class="presale-photo" role="img" aria-label="Photo of network cables plugged into a switch panel" style="background:linear-gradient(160deg,#3c8fe0,#1b3f9e 60%,#6a2fb0)"></div>
  <h3>Lorem ipsum dolor sit</h3>
  <p>Nunc ac ex nec orci tincidunt maximus ac nec eros. Integer a turpis leo. Sed varius arcu enim, eget sagittis elit porttitor vel. Ut eget volutpat nisi. Fusce orci libero, venenatis eu hendrerit in, feugiat vel nibh.</p>
</div>

<div class="divider abs" style="top:2437px"></div>

<div class="section-mark abs" style="top:2478px"></div>
<h2 class="section-title abs" style="top:2550px">Partners</h2>
<div class="partner-badge abs" role="img" aria-label="Partner badge" style="left:103px;top:2628px"></div>
<div class="partner-badge abs" role="img" aria-label="Partner badge" style="left:402px;top:2628px"></div>
<div class="partner-badge abs" role="img" aria-label="Partner badge" style="left:632px;top:2628px"></div>
<div class="partner-badge abs" role="img" aria-label="Partner badge" style="left:919px;top:2628px"></div>
<div class="partner-badge abs" role="img" aria-label="Partner badge" style="left:58px;top:2746px"></div>
<div class="partner-badge abs" role="img" aria-label="Partner badge" style="left:348px;top:2746px"></div>
<div class="partner-badge abs" role="img" aria-label="Partner badge" style="left:662px;top:2746px"></div>
<div class="partner-badge abs" role="img" aria-label="Partner badge" style="left:917px;top:2746px"></div>

<div class="divider abs" style="top:2870px"></div>

<div class="contact-field abs" role="img" aria-label="Faint circuit line pattern"></div>
<div class="section-mark abs" style="top:2906px"></div>
<h2 class="section-title abs" style="top:2974px">Contact Us</h2>
<div class="field abs" style="top:3033px;height:45px">full name</div>
<div class="field abs" style="top:3083px;height:42px">email</div>
<div class="field abs" style="top:3132px;height:104px">message</div>
<a class="btn send-btn abs">Send</a>
<div class="office abs">
  <h3>Head Office</h3>
  <p>48 Harlow Lane<br>Brenton, CP 20417</p>
  <p class="gap">Phone:1:555.014.2290<br>Email: address:info@korvel.example</p>
</div>
<div class="to-top abs"><svg width="12" height="8"><path d="M1 7l5-5 5 5" stroke="#fff" stroke-width="2" fill="none"/></svg></div>

<footer class="site-footer abs">
  <div class="footer-brand abs"><div class="sq"></div><span>KORVEL</span></div>
  <div class="social abs" style="left:523px" aria-label="Social link"></div>
  <div class="social abs" style="left:578px" aria-label="Social link"></div>
  <div class="social abs" style="left:632px" aria-label="Social link"></div>
  <div class="social abs" style="left:689px" aria-label="Social link"></div>
  <nav class="footer-nav">
    <a style="left:308px">Home</a>
    <a style="left:406px">Company</a>
    <a style="left:526px">Services</a>
    <a style="left:641px">Presales</a>
    <a style="left:760px">Partners</a>
    <a style="left:875px">Contact Us</a>
  </nav>
</footer>

</body>
</html>
```